Flyer für eine Zahnarztpraxis
Zielgruppe
Zahnarztpraxis, Zielgruppe sind Patienten im Erwachsenenalter
Aufgabenstellung
Den Text habe ich bereits geschrieben. Es soll ein DINA4 Flyer werden, mit sechs Seiten.

```html
<!DOCTYPE html>
<html lang="de">
<head>
<meta charset="utf-8">
<title>Flyer Vitamin D – Zahnarztpraxis Lindholm</title>
<link rel="stylesheet" href="https://fonts.googleapis.com/css2?family=Rubik:wght@400;500;600&display=swap">
<style>
:root{
  --bg:#a9a9a9;
  --yellow:#ebe300;
  --olive:#d2cb00;
  --cream:#f1eee9;
  --stone:#dcd8d2;
  --pink:#c65b84;
  --ink:#262626;
  --teal:#3f6d6b;
  --white:#ffffff;
}
*{box-sizing:border-box;margin:0;padding:0}
html,body{width:706px;height:1200px;overflow:hidden}
body{background:var(--bg);font-family:"Rubik",sans-serif;color:var(--ink);position:relative}
.spread{position:absolute;left:12px;width:682px;height:482px;display:flex;box-shadow:0 10px 24px rgba(0,0,0,.25)}
.spread--outside{top:90px}
.spread--inside{top:628px}
.panel{position:relative;width:227.33px;height:100%;overflow:hidden}
.panel--cream{background:var(--cream)}
.panel--yellow{background:var(--yellow)}
.panel--cover{background:var(--olive)}
.photo{position:absolute}
.sun{position:absolute;border-radius:50%;background:radial-gradient(circle,#f3c63a 0 45%,rgba(243,198,58,.35) 46% 70%,transparent 71%);z-index:1}
h2{font-weight:600;line-height:1.12}
.rule{height:1.5px;background:var(--pink);width:120px;margin:5px 0 8px}
.bullets{list-style:none}
.bullets li{position:relative;padding-left:13px;font-size:7.4px;line-height:1.3;margin-bottom:5px}
.bullets li::before{content:"";position:absolute;left:0;top:2px;width:6px;height:6px;border-radius:50%;background:var(--pink)}
p{font-size:7.6px;line-height:1.32}
.strong{font-weight:500}
.pink{color:var(--pink);font-weight:500}

/* outside panel 1 */
.situations .photo{top:0;left:0;width:100%;height:232px;background:linear-gradient(160deg,#4b5a2c,#2d2a1c 55%,#8a6a48)}
.situations .strip{position:absolute;bottom:0;left:0;width:100%;height:8px;background:var(--yellow)}
.situations .body{position:absolute;top:252px;left:24px;right:20px}
.situations h2{font-size:14px}

/* outside panel 2 */
.promise .photo{top:0;left:0;width:100%;height:225px;border-bottom-right-radius:60px;background:linear-gradient(180deg,#f6d48a,#e9a44a 45%,#6f7d3c)}
.promise .body{position:absolute;top:245px;left:16px;right:16px;text-align:center}
.promise h2{font-size:17px;margin-bottom:10px}
.promise p{font-weight:500;margin-bottom:9px}
.pill{display:inline-block;background:var(--pink);color:var(--white);font-size:8px;font-weight:500;padding:4px 8px;border-radius:4px;margin-top:6px}
.pill::before{content:"";display:inline-block;width:6px;height:6px;border:1.2px solid var(--white);border-radius:50%;margin-right:4px;vertical-align:-1px}

/* outside panel 3 */
.cover .brand{position:absolute;top:0;left:0;width:100%;height:62px;background:var(--stone);display:flex;align-items:center;gap:8px;padding-left:18px}
.brand-dot{width:22px;height:22px;border-radius:50%;border:1.5px solid var(--teal)}
.brand-name{color:var(--teal);font-size:9.5px;font-weight:400;line-height:1.15;letter-spacing:.3px}
.cover .title{position:absolute;top:76px;left:10px;right:10px;text-align:center}
.cover h1{font-size:21px;font-weight:600;line-height:1.05}
.cover .title p{font-size:8px;margin:6px auto 0;max-width:150px}
.cover .photo-main{top:190px;left:14px;width:190px;height:118px;border-radius:4px 40px 4px 40px;background:linear-gradient(180deg,#7fb0d8,#b9cbd6 55%,#8a8f8a);border:3px solid #e4dfd2}
.cover .photo-small{top:282px;left:114px;width:104px;height:68px;border-radius:4px 20px 4px 4px;background:linear-gradient(135deg,#d9c2ad,#8a6f5c);border:3px solid #e4dfd2}
.cover .question{position:absolute;top:328px;left:20px;width:140px;font-size:9.2px;font-weight:500;line-height:1.15}
.cover .teaser{position:absolute;bottom:0;left:10px;right:0;height:56px;background:var(--pink);border-top-left-radius:14px;color:#f6e7ee;font-size:11px;font-weight:500;line-height:1.12;padding:14px 58px 0 14px}

/* inside panel 1 */
.basics .body{position:absolute;top:28px;left:22px;right:18px}
.basics h2{font-size:14.5px}
.basics p{margin-bottom:8px}
.basics .photo{left:0;bottom:0;width:100%;height:242px;border-top-right-radius:60px;background:linear-gradient(160deg,#8aa3b1,#4d6a7a 60%,#6a5a4c)}

/* inside panel 2 */
.body-benefits .photo{top:16px;left:12px;width:204px;height:206px;border:4px solid var(--white);border-radius:6px 42px 6px 42px;background:linear-gradient(170deg,#7f9a5a,#9ab1bd 55%,#6e7d6d)}
.body-benefits .body{position:absolute;top:248px;left:22px;right:14px}
.body-benefits h2{font-size:13.5px}
.body-benefits .bullets li{margin-bottom:3px}
.body-benefits .note{margin-top:8px}

/* inside panel 3 */
.teeth .dots{position:absolute;top:10px;right:12px;width:16px;height:22px;background:radial-gradient(circle,#9aa3ad 1px,transparent 1.3px) 0 0/6px 6px}
.teeth .body{position:absolute;top:24px;left:18px;right:16px}
.teeth h2{font-size:14.5px;margin-bottom:10px;max-width:170px}
.fact{background:var(--pink);color:var(--white);font-size:8px;font-weight:500;line-height:1.2;padding:5px 8px;border-radius:3px;margin-bottom:10px}
.teeth p{margin-bottom:7px}
.icon-list{list-style:none}
.icon-list li{display:flex;align-items:center;gap:9px;font-size:7.6px;line-height:1.25;margin-bottom:6px}
.icon{flex:0 0 16px;height:16px;border-radius:50%;border:1.2px solid var(--teal);background:var(--white)}
.teeth .photo{right:0;bottom:0;width:100%;height:140px;border-top-left-radius:50px;background:linear-gradient(150deg,#9fc3e2,#e9e6df 55%,#c98e62)}
</style>
</head>
<body>

<section class="spread spread--outside" aria-label="Außenseite">
  <div class="panel panel--cream situations">
    <div class="photo" role="img" aria-label="Foto: Frau genießt mit geschlossenen Augen die Abendsonne"></div>
    <div class="sun" role="img" aria-label="Sonnen-Illustration" style="top:178px;left:165px;width:70px;height:70px"></div>
    <div class="body">
      <h2>Kennen Sie diese Situationen?</h2>
      <div class="rule"></div>
      <ul class="bullets">
        <li>Kommen Sie seltener an die frische Luft, als Sie es sich wünschen?</li>
        <li>Fühlen Sie sich häufig antriebslos oder niedergeschlagen, besonders in den Wintermonaten?</li>
        <li>Haben Sie gelegentlich empfindliche Zähne oder Zahnfleischprobleme?</li>
      </ul>
      <p class="strong" style="margin-top:8px">Vielleicht steckt hinter Ihren Beschwerden ein Vitamin-D-Mangel. Mit einem Bluttest in unserer Praxis, können wir herausfinden, ob Ihrem Körper etwas fehlt</p>
      <p class="strong" style="margin-top:8px">– und unterstützen Sie bei der passenden Ergänzung.</p>
    </div>
    <div class="strip"></div>
  </div>

  <div class="panel panel--yellow promise">
    <div class="photo" role="img" aria-label="Foto: Hände formen ein Herz vor der untergehenden Sonne"></div>
    <div class="body">
      <h2>Ihr Lächeln und Ihre Gesundheit sind es wert!</h2>
      <p>Vitamin D ist ein wichtiger Baustein für ein gesundes Leben – und gesunde Zähne.</p>
      <p>Unser Praxisteam berät Sie gern persönlich und beantwortet Ihre Fragen.</p>
      <p>Kommen Sie einfach auf uns zu – für Ihre Gesundheit von Kopf bis Fuß.</p>
      <span class="pill">zahnarztpraxis-lindholm.de</span>
    </div>
  </div>

  <div class="panel panel--cover cover">
    <div class="brand">
      <span class="brand-dot"></span>
      <span class="brand-name">ZAHNARZTPRAXIS<br>LINDHOLM &amp; TEAM</span>
    </div>
    <div class="title">
      <h1>Vitamin D -<br>mehr als nur ein Sonnenvitamin</h1>
      <p>Was Ihre Zähne und Ihr Körper jetzt brauchen könnten</p>
    </div>
    <div class="photo photo-main" role="img" aria-label="Foto: junge Frau mit Kopfhörern sitzt in der Sonne"></div>
    <div class="photo photo-small" role="img" aria-label="Foto: lachendes Kind"></div>
    <p class="question">Fühlen Sie sich oft müde? Haben Sie manchmal Zahnfleischprobleme oder empfindliche Zähne?</p>
    <div class="teaser">Vielleicht steckt mehr dahinter, als Sie denken...</div>
    <div class="sun" role="img" aria-label="Sonnen-Illustration" style="bottom:12px;right:-18px;width:62px;height:62px"></div>
  </div>
</section>

<section class="spread spread--inside" aria-label="Innenseite">
  <div class="panel panel--cream basics">
    <div class="body">
      <h2>Was ist Vitamin D eigentlich?</h2>
      <div class="rule"></div>
      <p>Vitamin D wird oft „Sonnenvitamin“ genannt, weil unser Körper es größtenteils selbst bildet – wenn Sonne auf unsere Haut trifft.</p>
      <p><span class="pink">Doch:</span> In unseren Breitengraden reicht die Sonnenstrahlung viele Monate im Jahr nicht aus, um genügend Vitamin D zu bilden.</p>
      <p><span class="pink">Wissen Sie wo Sie stehen?</span> Gemeinsam können wir Ihren Vitamin D Spiegel in wenigen Minuten bestimmen.</p>
    </div>
    <div class="photo" role="img" aria-label="Foto: Frau mit geschlossenen Augen, Hand auf der Brust, im Freien"></div>
    <div class="sun" role="img" aria-label="Sonnen-Illustration" style="top:208px;left:160px;width:60px;height:60px"></div>
  </div>

  <div class="panel panel--yellow body-benefits">
    <div class="photo" role="img" aria-label="Foto: Gruppe von Erwachsenen klatscht sich beim Sport ab"></div>
    <div class="body">
      <h2>Warum ist Vitamin D so wichtig für den Körper?</h2>
      <div class="rule" style="width:104px"></div>
      <ul class="bullets">
        <li>Unterstützt ein starkes Immunsystem</li>
        <li>Trägt zu kräftigen Knochen bei</li>
        <li>Fördert Muskelfunktion und Gleichgewicht</li>
        <li>Kann Müdigkeit und Antriebslosigkeit entgegenwirken</li>
      </ul>
      <p class="note">Fehlt Vitamin D, kann das langfristig Auswirkungen auf viele Bereiche unserer Gesundheit haben – oft, ohne dass wir es sofort merken.</p>
    </div>
  </div>

  <div class="panel panel--cream teeth">
    <div class="dots"></div>
    <div class="body">
      <h2>Vitamin D und Ihre Zähne – eine starke Verbindung</h2>
      <div class="fact">Wussten Sie, dass Vitamin D entscheidend für gesunde Zähne ist?</div>
      <p>Es sorgt dafür, dass Kalzium im Körper optimal aufgenommen wird – und Kalzium ist der Baustoff für feste Zähne und stabilen Kieferknochen.</p>
      <p class="strong">Ein Mangel kann unter anderem begünstigen:</p>
      <ul class="icon-list">
        <li><span class="icon"></span>Zahnfleischprobleme</li>
        <li><span class="icon"></span>Lockerung der Zähne</li>
        <li><span class="icon"></span>Schlechte Einheilung von Implantaten</li>
        <li><span class="icon"></span>Verzögerte Heilung nach zahnärztlichen Eingriffen</li>
      </ul>
    </div>
    <div class="sun" role="img" aria-label="Sonnen-Illustration" style="top:172px;right:16px;width:40px;height:40px"></div>
    <div class="photo" role="img" aria-label="Foto: Pipette mit Vitamin-D-Tropfen vor Sonnenlicht"></div>
  </div>
</section>

</body>
</html>
```